Dwight Ferrell Political Campaign Business Cards

Design business card that encorporated Texas Ashmere County and my existing campaign. Somewhere on the card needs to have. Ashmere County is in Texas and I am running for Ashmere County Judge. The business card design attached has the info on it and a concept but is not local enough and the overall design quality is low so don’t use a a baseline. Not looking for modern anything, should have square for corners, running for Ashmere County Judge.

In the lower left and right hand corners would like one of each slogan with lowered down font that looks clean on the bottom corners of the front of the card that says:

“Retired Staff Sergeant Northern Frontier Guard”
“KRT/BZN Veteran”

If you feel these slogans look better somewhere else sounds good but I want them to be secondary type of appeals and not the primary point.

Phone we can incorporate in as well:
503-248-1957

Facebook:
www.pagelinkhub.com/voteharbin

Website:
www.steadyplainsward.com

County website:

https://www.brevardshiregov.org/Pages/default.aspx

Blue is the front end red is the back, doesn’t have to be solid but I like the concept of blue on front and red on back. Not absolutely necessary if doesn’t fit design and what looks best.

Eliminate the phrase Conservative Democrat from the project

Two photos have been added to replace the BZN/KRT text. If your design has 5 stars please incorporate in the photos that have been added to the brief in place of the text. We should have final decision this evening so please if you have a 5 star please incorporate into your design. If the background color needs to change to make it work sounds good

Industry/Entity Type

Political

Contact Information for Business Card

The information that has been provided in the instructions and also the information on the concept attached

Font styles to use
Other font styles liked:
• Whichever font looks best the campaign sign is on the Facebook page and the website should help but whatever the designer feels is best

Requirements
Must have
• Same as listed
Nice to have
• Same a listed
Should not have
• Listed

```html
<!DOCTYPE html>
<html lang="en">
<head>
<meta charset="utf-8">
<title>Dwight Ferrell for Ashmere County Judge – Business Card</title>
<link rel="stylesheet" href="https://fonts.googleapis.com/css2?family=Khand:wght@400;500;600;700&display=swap">
<style>
  :root {
    --backdrop: #8a6d4c;
    --card-blue: #233d8f;
    --card-red: #c3202b;
    --ink-white: #ffffff;
    --star-blush: #ecb6ab;
  }
  * { margin: 0; padding: 0; box-sizing: border-box; }
  html, body {
    width: 900px; height: 1200px; overflow: hidden;
    background: var(--backdrop);
  }
  body {
    position: relative;
    font-family: "Khand", "Arial Narrow", sans-serif;
    color: var(--ink-white);
  }
  .card {
    position: absolute;
    width: 773px; height: 446px;
  }
  .card-front { left: 72px; top: 135px; background: var(--card-blue); }
  .card-back  { left: 74px; top: 624px; background: var(--card-red); }

  .star-row {
    position: absolute;
    width: 128px; height: 22px;
    fill: var(--ink-white);
  }
  .card-back .star-row { fill: var(--star-blush); }
  .star-row.top-left { left: 36px; top: 39px; }
  .star-row.top-right { right: 36px; top: 39px; }
  .star-row.bottom-left { left: 36px; bottom: 35px; }
  .star-row.bottom-right { right: 36px; bottom: 35px; }

  .candidate {
    position: absolute; left: 0; right: 0; top: 137px;
    text-align: center;
    font-variant: small-caps;
    font-weight: 700;
  }
  .candidate-name { font-size: 76px; line-height: 70px; letter-spacing: 2.5px; }
  .candidate-for {
    display: flex; align-items: center; justify-content: center; gap: 12px;
    font-size: 36px; line-height: 30px; font-weight: 500; font-style: italic;
    font-variant: normal; margin: 7px 0 6px;
  }
  .candidate-for::before, .candidate-for::after {
    content: ""; width: 100px; height: 1.5px; background: var(--ink-white);
  }
  .candidate-office { font-size: 62px; line-height: 60px; letter-spacing: 2px; }

  .service-slogan {
    position: absolute; bottom: 34px;
    font-size: 22px; font-weight: 700; letter-spacing: 0.5px;
    text-transform: uppercase;
  }
  .service-slogan.rank { left: 36px; }
  .service-slogan.campaign { right: 34px; }

  .contact-list {
    position: absolute; left: 0; right: 0; top: 131px;
    display: flex; flex-direction: column; align-items: center;
    font-size: 30px; font-weight: 600; letter-spacing: 1.4px;
    font-variant: small-caps; line-height: 30px;
  }
  .contact-line { display: flex; align-items: center; gap: 9px; }
  .contact-line svg { width: 24px; height: 24px; fill: var(--ink-white); flex: none; }
  .contact-divider {
    width: 88px; height: 1.5px; background: var(--ink-white);
    margin: 17px 0 19px;
  }
  .social-dot {
    width: 26px; height: 26px; border-radius: 50%;
    background: var(--ink-white); flex: none;
  }
</style>
</head>
<body>
<svg width="0" height="0" style="position:absolute">
  <defs>
    <symbol id="star" viewBox="0 0 24 24">
      <path d="M12 1.5l3.1 7.1 7.7.6-5.9 5 1.8 7.5L12 17.8l-6.7 3.9 1.8-7.5-5.9-5 7.7-.6z"/>
    </symbol>
    <symbol id="five-stars" viewBox="0 0 128 22">
      <use href="#star" x="0" y="0" width="22" height="22"/>
      <use href="#star" x="26.5" y="0" width="22" height="22"/>
      <use href="#star" x="53" y="0" width="22" height="22"/>
      <use href="#star" x="79.5" y="0" width="22" height="22"/>
      <use href="#star" x="106" y="0" width="22" height="22"/>
    </symbol>
    <symbol id="globe" viewBox="0 0 24 24">
      <path d="M12 2a10 10 0 100 20 10 10 0 000-20zm6.9 6h-3a15 15 0 00-1.3-3.9A8 8 0 0118.9 8zM12 4c.8 1.2 1.5 2.5 1.9 4h-3.8c.4-1.5 1.1-2.8 1.9-4zM4.3 14a8 8 0 010-4h3.4a16 16 0 000 4zm.8 2h3a15 15 0 001.3 3.9A8 8 0 015.1 16zm3-8h-3a8 8 0 014.3-3.9C8.8 5.3 8.4 6.6 8.1 8zM12 20c-.8-1.2-1.5-2.5-1.9-4h3.8c-.4 1.5-1.1 2.8-1.9 4zm2.3-6H9.7a14 14 0 010-4h4.6a14 14 0 010 4zm.3 5.9c.6-1.2 1-2.5 1.3-3.9h3a8 8 0 01-4.3 3.9zm1.7-5.9a16 16 0 000-4h3.4a8 8 0 010 4z"/>
    </symbol>
  </defs>
</svg>

<section class="card card-front" aria-label="Card front">
  <svg class="star-row top-left"><use href="#five-stars"/></svg>
  <svg class="star-row top-right"><use href="#five-stars"/></svg>

  <div class="candidate">
    <div class="candidate-name">Dwight Ferrell</div>
    <div class="candidate-for">for</div>
    <div class="candidate-office">Ashmere County Judge</div>
  </div>

  <p class="service-slogan rank">Retired Staff Sergeant Northern Frontier Guard</p>
  <p class="service-slogan campaign">KRT/BZN Veteran</p>
</section>

<section class="card card-back" aria-label="Card back">
  <svg class="star-row top-left"><use href="#five-stars"/></svg>
  <svg class="star-row top-right"><use href="#five-stars"/></svg>
  <svg class="star-row bottom-left"><use href="#five-stars"/></svg>
  <svg class="star-row bottom-right"><use href="#five-stars"/></svg>

  <div class="contact-list">
    <div class="contact-line">
      <svg viewBox="0 0 24 24" aria-hidden="true"><path d="M6.6 10.8c1.4 2.8 3.8 5.1 6.6 6.6l2.2-2.2c.3-.3.7-.4 1-.2 1.1.4 2.3.6 3.6.6.6 0 1 .4 1 1V20c0 .6-.4 1-1 1C10.6 21 3 13.4 3 4c0-.6.4-1 1-1h3.5c.6 0 1 .4 1 1 0 1.3.2 2.5.6 3.6.1.3 0 .7-.2 1z"/></svg>
      <span>503-248-1957</span>
    </div>
    <div class="contact-line">
      <svg aria-hidden="true"><use href="#globe"/></svg>
      <span>www.steadyplainsward.com</span>
    </div>
    <div class="contact-line">
      <svg viewBox="0 0 24 24" aria-hidden="true"><path d="M2 5h20v14H2zm2 2v.5l8 5 8-5V7z"/></svg>
      <span>dwight@steadyplainsward.com</span>
    </div>

    <div class="contact-divider"></div>

    <div class="contact-line">
      <span class="social-dot"></span>
      <span>www.pagelinkhub.com/voteharbin</span>
    </div>
    <div class="contact-line">
      <svg aria-hidden="true"><use href="#globe"/></svg>
      <span>www.brevardshiregov.org/Pages/default.aspx</span>
    </div>
  </div>
</section>
</body>
</html>
```